New Managed IT company needs a business card

We are an IT management and support company that needs a business card design. I have a logo that I'll provide. Blues and blacks match the logo, but i'm open to anything. I want the card to help people take us seriously, but still have some energy and fun in it. The card should communicate stability and a solid company.

Target Market(s)

Target market includes Owners and Presidents at small businesses of 20 - 100 employees in the Pittsburgh PA area.

Industry/Entity Type

Information Technology

Contact Information for Business Card

i am open to other designs, but i imagine having only the logo on one side and then the logo plus all contact details on the other side.

Requirements
Must have
• Our logo
• Company name is optional if the logo makes it obvious
• A name - Lew Tasker
• A title - President
• A phone number - 724-XXX-XXXX
• A mobile phone number - 724-516-0471
• An email address - ltasker@brightlanetech.com
• a website - brightlanetech.com or www.brightlanetech.com
Nice to have
• some people tell me the logo feels like a superhero theme, some fun with that idea might be good. I'm open to ideas.
Should not have
• stock photos of people or computers - especially old looking stuff.

```html
<!DOCTYPE html>
<html lang="en">
<head>
<meta charset="utf-8">
<title>Brightlane Tech – Business Card</title>
<link href="https://fonts.googleapis.com/css2?family=Michroma&display=swap" rel="stylesheet">
<style>
  :root {
    --stage: #2a2a2c;
    --card-dark: #1b191d;
    --card-mid: #2b2a2f;
    --silver: #a9abb0;
    --white: #e9eaee;
    --blue: #1b8fd6;
    --mark-fill: #2f6fa3;
  }
  * { margin: 0; padding: 0; box-sizing: border-box; }
  html, body { width: 1200px; height: 900px; overflow: hidden; }
  body {
    background: var(--stage);
    font-family: "Michroma", "Arial", sans-serif;
    display: flex;
    align-items: center;
    justify-content: center;
    gap: 40px;
  }
  .card {
    position: relative;
    width: 560px;
    height: 320px;
    border-radius: 2px;
    overflow: hidden;
  }
  .card-back {
    background: linear-gradient(135deg, var(--card-mid) 0%, var(--card-dark) 55%, var(--card-mid) 100%);
    display: flex;
    align-items: center;
    justify-content: center;
  }
  .brand {
    display: flex;
    align-items: center;
    gap: 18px;
  }
  .brand-dot {
    width: 74px;
    height: 74px;
    border-radius: 50%;
    background: var(--mark-fill);
  }
  .brand-name {
    color: var(--silver);
    font-size: 24px;
    letter-spacing: 4px;
    line-height: 1.3;
    text-transform: uppercase;
  }
  .card-front {
    background: var(--card-dark);
  }
  .front-name {
    position: absolute;
    left: 40px;
    top: 52px;
    color: var(--silver);
    font-size: 20px;
    letter-spacing: 4px;
    line-height: 1.3;
    text-transform: uppercase;
  }
  .front-dot {
    position: absolute;
    right: 40px;
    top: 38px;
    width: 150px;
    height: 150px;
    border-radius: 50%;
    background: var(--mark-fill);
  }
  .person {
    position: absolute;
    left: 40px;
    top: 152px;
    text-transform: uppercase;
    font-size: 11px;
    letter-spacing: 1px;
    line-height: 1.5;
  }
  .person-name { color: var(--blue); }
  .person-title { color: var(--white); }
  .contacts {
    position: absolute;
    left: 40px;
    list-style: none;
    color: var(--white);
    font-size: 11px;
    letter-spacing: 0.5px;
    text-transform: uppercase;
  }
  .contacts li {
    display: flex;
    align-items: center;
    gap: 8px;
    height: 17px;
  }
  .contacts svg { width: 11px; height: 11px; fill: var(--blue); flex: none; }
  .contacts-phone { top: 208px; }
  .contacts-web { top: 258px; }
</style>
</head>
<body>
  <section class="card card-back" aria-label="Card back">
    <div class="brand">
      <div class="brand-dot"></div>
      <div class="brand-name">Brightlane<br>Tech</div>
    </div>
  </section>

  <section class="card card-front" aria-label="Card front">
    <div class="front-name">Brightlane<br>Tech</div>
    <div class="front-dot"></div>

    <div class="person">
      <div class="person-name">Lew Tasker</div>
      <div class="person-title">President</div>
    </div>

    <ul class="contacts contacts-phone">
      <li>
        <svg viewBox="0 0 12 12"><path d="M1 4c0-2 2-3 5-3s5 1 5 3l-3 1-1-1.5H5L4 5zM3 6h6l1 5H2z"/></svg>
        724-XXX-XXXX
      </li>
      <li>
        <svg viewBox="0 0 12 12"><path d="M3 0h6v12H3zM4 1.5v8h4v-8z"/></svg>
        724-516-0471
      </li>
    </ul>

    <ul class="contacts contacts-web">
      <li>
        <svg viewBox="0 0 12 12"><path d="M0 2h12v1L6 7 0 3zM0 4.5l6 4 6-4V10H0z"/></svg>
        ltasker@brightlanetech.com
      </li>
      <li>
        <svg viewBox="0 0 12 12"><circle cx="6" cy="6" r="5.5"/><path d="M1 6h10M6 .5v11" stroke="#1b191d" stroke-width="0.8"/><ellipse cx="6" cy="6" rx="2.5" ry="5.5" fill="none" stroke="#1b191d" stroke-width="0.8"/></svg>
        www.brightlanetech.com
      </li>
    </ul>
  </section>
</body>
</html>
```